Banner for a program to be used as a cover photo for Facebook

Banner design for a program I run called: The Craft of Bold Ascent
This is a 90 day implementation program for business owners who set one main goal to reach during that time. The focus of the program is to help them set the goal, create the strategy to reach the goal and take keystone actions to achieve the goal. This program (I run multiple at a time) is exclusive to only 8 people at a time...the price point of the program is $6,000.

Company Name: Lantern Harbor

My title: Enterprise Momentum Coach (EMC!)

My area of expertise: Helping business owners who already know what they do, who they serve, and have momentum (and sales) accelerate the growth of their business by eliminate what they don't need and simplifying the strategy to achieve mind blowing results. (Success habits, behaviors, routines, attitudes, speed of implementation, simplification, essentialism, focus, goal setting, high performance)

Who I want to attract: People who have made $25k - $75k in the last 12 months of their business (service based) who are action takers, big thinkers, in it to win it, take action even in the face of fear, committed, decision makers

Target Market(s)

Women business owners who have been in business for 2 - 5 years making at least $25k - $75k in their previous 12 months. They are feminine, married, moms, higher end and looking for a more exclusive and selective group of like-minded people to grow with. They are attracted to a more glamorous, boutique feel and desire to catapult the results in their business.

Industry/Entity Type

Business

Font styles to use
Sans Serif

Requirements
Must have
• Crisp, Clean, High End, Simple, Elegant, Picture of me
• Text on Banner:
• The Craft of Bold Ascent
• with Carla Voss, Enterprise Momentum Coach
Should not have
• Men in suits in pictures.
• Corporate Feel.

```html
<!DOCTYPE html>
<html lang="en">
<head>
<meta charset="UTF-8">
<title>The Craft of Bold Ascent – Cover Banner</title>
<link href="https://fonts.googleapis.com/css2?family=Oswald:wght@300;400;500&display=swap" rel="stylesheet">
<style>
  :root {
    --stage: #1e1e1e;
    --paper: #ffffff;
    --accent: #5ab4cc;
    --ink: #444444;
    --teal-light: #6fc0d4;
    --teal-mid: #2a9fb8;
    --teal-deep: #0a86a0;
    --portrait-light: #cfe9f0;
    --portrait-deep: #8cc9da;
  }
  html, body {
    margin: 0;
    padding: 0;
    width: 1200px;
    height: 900px;
    overflow: hidden;
    background: var(--stage);
  }
  .banner {
    position: absolute;
    left: 185px;
    top: 290px;
    width: 830px;
    height: 320px;
    background: var(--paper);
    overflow: hidden;
    font-family: "Oswald", sans-serif;
  }
  .banner__copy {
    position: absolute;
    left: 12px;
    top: 36px;
    width: 345px;
  }
  .banner__title {
    margin: 0;
    height: 60px;
    background: var(--accent);
    color: var(--paper);
    font-weight: 400;
    font-size: 33px;
    line-height: 60px;
    text-align: center;
    letter-spacing: -0.4px;
  }
  .banner__description {
    margin: 14px 0 0;
    color: var(--ink);
    font-weight: 300;
    font-size: 19px;
    line-height: 29px;
    text-align: center;
    letter-spacing: -0.2px;
  }
  .banner__exclusive {
    margin: 8px 0 0;
    color: var(--accent);
    font-weight: 500;
    font-size: 20px;
    line-height: 30px;
    text-align: center;
    letter-spacing: -0.2px;
  }
  .banner__credit {
    margin: 6px 0 0;
    color: var(--ink);
    font-weight: 400;
    font-size: 16px;
    line-height: 24px;
    text-align: center;
  }
  .banner__artwork {
    position: absolute;
    left: 450px;
    top: 0;
    width: 380px;
    height: 320px;
    background: radial-gradient(ellipse at 40% 0%, var(--teal-light) 0%, var(--teal-mid) 45%, var(--teal-deep) 100%);
  }
  .banner__portrait {
    position: absolute;
    left: 535px;
    top: 50px;
    width: 220px;
    height: 220px;
    border-radius: 50%;
    border: 4px solid var(--paper);
    box-sizing: border-box;
    background: linear-gradient(160deg, var(--portrait-light) 0%, var(--portrait-deep) 100%);
  }
</style>
</head>
<body>
  <section class="banner">
    <div class="banner__artwork" role="img" aria-label="Teal backdrop of shattering shards suggesting forward momentum"></div>
    <div class="banner__portrait" role="img" aria-label="Portrait photo of Carla Voss"></div>
    <div class="banner__copy">
      <h1 class="banner__title">The Craft of Bold Ascent</h1>
      <p class="banner__description">90 day implementation program for<br>business owners who set one main goal<br>to reach during that time</p>
      <p class="banner__exclusive">Exclusive to only 8 people at a time!</p>
      <p class="banner__credit">with Carla Voss, Enterprise Momentum Coach</p>
    </div>
  </section>
</body>
</html>
```